PLUM BUSINESS CARD

Need a business card and logo. The company name is PLUM (Piedmont League of Ultimate Mareriders). It's a business that offers horseback riding lessons to young girls. Please put my name: Renata Bowley and a place for email and phone number. I would like the card to look feminine and soft. I like script type lettering. I want the card to be white or ivory with black or gray and hot pink print. A horse head outline would be cool, something whimsical. Think teen girl who likes glamour. Also, I give western riding lessons. So I like faded out background Images of western saddles, cowgirls, horses with long hair, ropes, horses in sunset...mabe the word PLUM can be made out of a lasso rope?

Just updated my project with a little more detail

Target Market(s)

Young girls/ cowgirls, western riding

Industry/Entity Type

Horseback Riding

Font styles to use
Script

Colors
e34197

Requirements
Must have
• A logo of PLUM.
Must say Piedmont League of Ultimate Mareriders
Colors are Pink and Black with an elegant, glamorous, feminine look.
Nice to have
• Could have a picture or outline of a horse

```html
<!DOCTYPE html>
<html lang="en">
<head>
<meta charset="utf-8">
<title>PLUM Business Card</title>
<link href="https://fonts.googleapis.com/css2?family=Jost:wght@400;500&display=swap" rel="stylesheet">
<style>
  :root {
    --hot-pink: #e34197;
    --card-black: #0a0a0a;
    --swirl: #161616;
    --ink-white: #ffffff;
    --ink-grey: #8a8a8a;
    --ink-soft: #d9d9d9;
    --stage: #f4f4f4;
    --label-ink: #1a1a1a;
    --label-line: #cfcfcf;
  }
  * { box-sizing: border-box; margin: 0; padding: 0; }
  html, body { width: 1200px; height: 1000px; overflow: hidden; }
  body {
    position: relative;
    background: radial-gradient(ellipse at 50% 40%, #ffffff 0%, var(--stage) 70%, #e9e9e9 100%);
    font-family: "Jost", "Futura", sans-serif;
  }

  /* ---------- Business card ---------- */
  .card {
    position: absolute;
    left: 190px; top: 110px;
    width: 820px; height: 470px;
    background: var(--card-black);
    overflow: hidden;
    box-shadow: 0 18px 40px rgba(0,0,0,.22);
  }
  .card__backdrop {
    position: absolute; inset: 0;
    background:
      radial-gradient(ellipse 260px 420px at 78% 30%, var(--swirl) 0%, transparent 70%),
      radial-gradient(ellipse 200px 300px at 40% 0%, var(--swirl) 0%, transparent 70%);
  }
  .card__band {
    position: absolute; left: 0; right: 0; bottom: 0;
    height: 12px; background: var(--hot-pink);
  }
  .card__name-plate {
    position: absolute; left: 330px; top: 100px;
    background: var(--hot-pink);
    padding: 4px 22px 2px;
  }
  .card__name {
    color: var(--ink-white);
    font-weight: 500; font-size: 50px; letter-spacing: 1px;
    text-transform: uppercase; line-height: 1.05;
  }
  .card__role {
    position: absolute; left: 470px; top: 176px;
    color: var(--ink-grey);
    font-size: 20px; letter-spacing: 2px; text-transform: uppercase;
  }

  .brand {
    position: absolute; left: 44px; top: 230px;
    width: 330px;
  }
  .brand__name {
    color: var(--hot-pink);
    font-weight: 500; font-size: 64px; letter-spacing: 4px; line-height: 1;
  }
  .brand__rule {
    height: 3px; background: var(--hot-pink); margin-top: 8px; width: 260px;
  }
  .brand__rule + .brand__rule { margin-top: 5px; }
  .brand__tagline {
    color: var(--ink-soft);
    font-size: 16px; line-height: 1.2; margin-top: 8px; text-align: center; width: 270px;
  }

  .contact {
    position: absolute; left: 510px; top: 385px;
    color: var(--ink-white);
    font-size: 15px; letter-spacing: 1px;
  }
  .contact__row { display: flex; align-items: center; gap: 10px; margin-bottom: 8px; }
  .contact__row--indent { padding-left: 0; }
  .contact__item { display: inline-flex; align-items: center; gap: 8px; }
  .contact__icon { width: 14px; height: 14px; fill: var(--ink-white); flex: none; }
  .contact__gap { width: 22px; }

  /* ---------- Logo lockup ---------- */
  .lockup {
    position: absolute; left: 46px; top: 830px; width: 260px;
  }
  .lockup__name {
    color: var(--hot-pink);
    font-weight: 500; font-size: 58px; letter-spacing: 4px; line-height: 1;
  }
  .lockup__rule { height: 3px; background: var(--hot-pink); width: 196px; margin-top: 8px; }
  .lockup__rule + .lockup__rule { margin-top: 4px; }
  .lockup__tagline {
    color: #555; font-size: 12.5px; line-height: 1.2; margin-top: 6px; width: 200px; text-align: center;
  }

  /* ---------- Presentation label ---------- */
  .label {
    position: absolute; left: 848px; top: 912px;
    width: 352px; height: 42px;
    background: #fff; border: 1px solid var(--label-line); border-right: 0;
    display: flex; align-items: center; justify-content: center;
    color: var(--label-ink); font-size: 21px; letter-spacing: 1px;
  }
</style>
</head>
<body>

  <section class="card">
    <div class="card__backdrop" role="img" aria-label="Faint dark swirling horse-mane decoration across the card background"></div>

    <div class="card__name-plate"><h1 class="card__name">Renata Bowley</h1></div>
    <p class="card__role">Instructor</p>

    <div class="brand">
      <div class="brand__name">PLUM</div>
      <div class="brand__rule"></div>
      <div class="brand__rule"></div>
      <p class="brand__tagline">Piedmont League of Ultimate Mareriders</p>
    </div>

    <div class="contact">
      <div class="contact__row">
        <span class="contact__item">
          <svg class="contact__icon" viewBox="0 0 24 24" aria-hidden="true"><path d="M6.6 10.8a15.1 15.1 0 0 0 6.6 6.6l2.2-2.2a1 1 0 0 1 1-.25 11.4 11.4 0 0 0 3.6.57 1 1 0 0 1 1 1V20a1 1 0 0 1-1 1A17 17 0 0 1 3 4a1 1 0 0 1 1-1h3.5a1 1 0 0 1 1 1c0 1.25.2 2.45.57 3.57a1 1 0 0 1-.25 1z"/></svg>
          +1 555 014 2118
        </span>
        <span class="contact__gap"></span>
        <span class="contact__item">
          <svg class="contact__icon" viewBox="0 0 24 24" aria-hidden="true"><path d="M7 2h10a2 2 0 0 1 2 2v16a2 2 0 0 1-2 2H7a2 2 0 0 1-2-2V4a2 2 0 0 1 2-2zm0 3v12h10V5zm5 13.2a1.2 1.2 0 1 0 0 2.4 1.2 1.2 0 0 0 0-2.4z"/></svg>
          +1 555 016 7204
        </span>
      </div>
      <div class="contact__row">
        <span class="contact__item">
          <svg class="contact__icon" viewBox="0 0 24 24" aria-hidden="true"><path d="M12 2a10 10 0 1 0 5 18.7l-.9-1.7A8 8 0 1 1 20 12v1.2a1.8 1.8 0 0 1-3.6 0V7.5h-2v.9A5 5 0 1 0 15 16a3.8 3.8 0 0 0 7-2.8V12A10 10 0 0 0 12 2zm0 13a3 3 0 1 1 0-6 3 3 0 0 1 0 6z"/></svg>
          renatabowley@plumriding.com
        </span>
      </div>
    </div>

    <div class="card__band"></div>
  </section>

  <section class="lockup">
    <div class="lockup__name">PLUM</div>
    <div class="lockup__rule"></div>
    <div class="lockup__rule"></div>
    <p class="lockup__tagline">Piedmont League of Ultimate Mareriders</p>
  </section>

  <div class="label">PLUM BUSINESS CARD</div>

</body>
</html>
```